New Personal and business business card

I need a new business card design for my business and myslef personally. One side is my business and the other side is my personal information.

Contact Information for Business Card

i will include a copy of my current business card

Colors

Designer to choose colors to be used in the design.

Requirements
Must have
• all of the information currently on my card
Should not have
• i prefer not to have gold color. i know the logo has gold but use gray one

```html
<!DOCTYPE html>
<html lang="en">
<head>
<meta charset="utf-8">
<title>Marlow Keaton – Business Cards</title>
<link href="https://fonts.googleapis.com/css2?family=Russo+One&family=Open+Sans:wght@400;600&display=swap" rel="stylesheet">
<style>
  :root {
    --card-dark: #2a2527;
    --accent: #00f09a;
    --text-light: #f2f2f2;
    --name-gray: #a9a9a9;
    --canvas-bg: #e4e2df;
  }
  * { box-sizing: border-box; margin: 0; padding: 0; }
  html, body { width: 1200px; height: 1067px; overflow: hidden; }
  body {
    background: var(--canvas-bg);
    font-family: "Open Sans", sans-serif;
    position: relative;
  }
  .card {
    position: absolute;
    left: 250px;
    width: 700px;
    height: 400px;
    background: var(--card-dark);
    color: var(--text-light);
    box-shadow: 0 10px 30px rgba(0,0,0,.25);
    overflow: hidden;
  }
  /* Personal side */
  .card--personal { top: 70px; }
  .personal-name {
    position: absolute; top: 38px; left: 300px; width: 370px;
    text-align: center; white-space: nowrap;
    font-family: "Russo One", sans-serif; font-weight: 400;
    font-size: 38px; color: var(--accent); letter-spacing: 1px;
  }
  .credentials {
    position: absolute; list-style: none;
    font-size: 16px; line-height: 1.4; font-weight: 600;
  }
  .credentials--left { top: 108px; left: 40px; width: 340px; }
  .credentials--right { top: 160px; left: 395px; width: 290px; }
  .contact-band {
    position: absolute; left: 0; right: 0; top: 318px; height: 50px;
    background: var(--accent);
    display: flex; align-items: center; justify-content: space-between;
    padding: 0 40px;
    font-family: "Russo One", sans-serif;
    color: var(--card-dark); font-size: 20px;
  }
  /* Business side */
  .card--business { top: 560px; }
  .logo-square {
    position: absolute; top: 70px; left: 150px;
    width: 110px; height: 110px; background: var(--accent);
  }
  .business-name {
    position: absolute; top: 198px; left: 45px; width: 320px; text-align: center;
    white-space: nowrap;
    font-family: "Russo One", sans-serif; font-weight: 400;
    font-size: 30px; color: var(--name-gray);
  }
  .business-role {
    position: absolute; top: 246px; left: 45px; width: 320px; text-align: center;
    font-size: 18px;
  }
  .divider {
    position: absolute; top: 70px; left: 385px;
    width: 5px; height: 260px; background: var(--accent);
  }
  .services {
    position: absolute; top: 80px; left: 420px; list-style: none;
    font-size: 19px; line-height: 1.38;
  }
  .services li::before { content: "• "; }
  .contact-line {
    position: absolute; display: flex; align-items: center; gap: 10px;
    font-size: 17px;
  }
  .contact-line--web { left: 30px; top: 340px; }
  .contact-line--phone { right: 40px; top: 340px; }
  .contact-icon { width: 26px; height: 26px; }
</style>
</head>
<body>
  <section class="card card--personal">
    <h1 class="personal-name">MARLOW KEATON</h1>
    <ul class="credentials credentials--left">
      <li>· Designated Pilot Examiner<br>&nbsp;&nbsp;Rotocraft Helicopter</li>
      <li>· CFII Airplane and helicopter</li>
      <li>· mei, igi, agi</li>
      <li>· ATP Multiengine LAND/AT<br>&nbsp;&nbsp;Single Engine LAND/ATP Helicopter</li>
    </ul>
    <ul class="credentials credentials--right">
      <li>· Seaplane Instructors</li>
      <li>· Hollis Grant Insurance Check<br>&nbsp;&nbsp;Pilot For Corvan Helicopter</li>
      <li>· Contract Pilot And Instructor</li>
      <li>· CX-520s, EM-500 Single Pilot<br>&nbsp;&nbsp;And LX-JET Type Rating</li>
    </ul>
    <div class="contact-band">
      <span class="contact-email">M.J.KEATON@MAILBOX.COM</span>
      <span class="contact-phone">PH:555.201.4417</span>
    </div>
  </section>

  <section class="card card--business">
    <div class="logo-square"></div>
    <h2 class="business-name">MARLOW KEATON</h2>
    <p class="business-role">Chief Pilot/Owner</p>
    <div class="divider"></div>
    <ul class="services">
      <li>Scenic Tours/Event Rides</li>
      <li>Photography</li>
      <li>Flight Instruction</li>
      <li>Airplane &amp; Helicopter</li>
      <li>Special Events</li>
      <li>Frost Patrol/Crop</li>
      <li>Pollination</li>
      <li>Aircraft Sales</li>
    </ul>
    <div class="contact-line contact-line--web">
      <svg class="contact-icon" viewBox="0 0 26 26" aria-hidden="true">
        <circle cx="13" cy="13" r="13" fill="#00f09a"/>
        <circle cx="13" cy="13" r="7" fill="none" stroke="#2a2527" stroke-width="1.6"/>
        <ellipse cx="13" cy="13" rx="3" ry="7" fill="none" stroke="#2a2527" stroke-width="1.4"/>
        <line x1="6" y1="13" x2="20" y2="13" stroke="#2a2527" stroke-width="1.4"/>
      </svg>
      <span>www.SKYWARDROTORS.com</span>
    </div>
    <div class="contact-line contact-line--phone">
      <svg class="contact-icon" viewBox="0 0 26 26" aria-hidden="true">
        <circle cx="13" cy="13" r="13" fill="#00f09a"/>
        <rect x="9" y="6" width="8" height="14" rx="1.5" fill="#2a2527"/>
        <rect x="10.5" y="8" width="5" height="8" fill="#00f09a"/>
      </svg>
      <span>PH.555.303.8820</span>
    </div>
  </section>
</body>
</html>
```